Advertisement for Fresh Horizons Award 2019 needed

I am Lobbying for the needs of youngsters in a specific region. This year I am planning the first fresh horizons award to give young people the chance to present their regional projekts/activities/initiatives and to award them some price money they can use for further activites. This Initiative is not only targeted at young people but also organizations who work with youngsters. Therefore I would need an advertisment we could use to promote this event in newspapers, website and via an E-Mail Campaign. Possibly also on social media, so I am thinking of a Facebook and Instagram Design as well. I uploaded some logos and materials that we are using already. to give you an idea of the colors. The ad should be targeted towards a young audience but also draw the attention of people who work with youngsters. Size MAX. (length x width) 21cm x 7cm
Youngsters age 14-26 yrs
People who work with youngsters (youth organizations, schools, clubs, social workers, municipalities)

```html
<!DOCTYPE html>
<html lang="de">
<head>
<meta charset="utf-8">
<title>Fresh Horizons Award 2019</title>
<link rel="stylesheet" href="https://fonts.googleapis.com/css2?family=Fredoka+One&family=Josefin+Sans:wght@400;600;700&display=swap">
<style>
  :root {
    --page: #f4f4f4;
    --sun: #fdd54a;
    --sun-deep: #fbc23a;
    --blush: #f6a56a;
    --orange: #f26b21;
    --ink: #231815;
    --teal: #16b49c;
    --gold: #ffd740;
  }
  * { margin: 0; padding: 0; box-sizing: border-box; }
  html, body { width: 1200px; height: 1000px; overflow: hidden; background: var(--page); }
  .canvas { position: relative; width: 1200px; height: 1000px; }

  .banner {
    position: absolute; left: 20px; top: 283px; width: 1158px; height: 385px;
    overflow: hidden;
    background:
      radial-gradient(ellipse 420px 260px at 1080px 30px, rgba(246,150,110,.55), transparent 70%),
      radial-gradient(ellipse 380px 260px at 40px 360px, rgba(255,230,120,.7), transparent 70%),
      linear-gradient(100deg, var(--sun-deep) 0%, var(--sun) 45%, var(--sun-deep) 100%);
    font-family: "Josefin Sans", sans-serif;
    color: var(--ink);
  }

  .award-title {
    position: absolute; left: 0; right: 0; top: 22px; text-align: center;
    font-family: "Fredoka One", cursive;
    font-size: 62px; letter-spacing: 2px; line-height: 1;
    color: var(--orange);
    -webkit-text-stroke: 2px var(--ink);
    text-shadow: -6px 5px 0 var(--teal);
  }

  .year-tag { position: absolute; left: 912px; top: 80px; width: 175px; height: 62px; }
  .year-tag svg { position: absolute; inset: 0; }
  .year-tag span {
    position: absolute; inset: 0; display: flex; align-items: center; justify-content: center;
    font-family: "Fredoka One", cursive; font-size: 44px; color: var(--gold);
    -webkit-text-stroke: 1.5px var(--orange);
  }

  .tagline {
    position: absolute; left: 0; width: 1170px; top: 108px; text-align: center;
    font-weight: 700; font-size: 20px;
  }
  .eligibility {
    position: absolute; left: 0; width: 1170px; top: 148px; text-align: center;
    font-size: 19px; line-height: 30px; font-weight: 600;
  }
  .eligibility .caps { text-transform: uppercase; }

  .highlight {
    position: absolute; left: 310px; width: 542px; top: 211px; height: 42px;
    border-top: 2px solid var(--orange); border-bottom: 2px solid var(--orange);
    display: flex; align-items: center; justify-content: center;
    font-weight: 700; font-size: 15px; color: var(--orange); text-transform: uppercase;
  }

  .event-date { position: absolute; left: 378px; top: 275px; width: 418px; height: 79px; }
  .event-date svg { position: absolute; inset: 0; }
  .event-date p {
    position: absolute; inset: 0; display: flex; flex-direction: column;
    align-items: center; justify-content: center;
    font-family: "Fredoka One", cursive; font-size: 23px; line-height: 31px;
    color: var(--gold); text-transform: uppercase; letter-spacing: .5px;
  }

  .partner {
    position: absolute; display: flex; align-items: center; justify-content: center; gap: 10px;
    font-family: "Josefin Sans", sans-serif; font-weight: 700; color: var(--ink);
    text-align: center;
  }
  .partner .mark { width: 14px; height: 14px; background: var(--ink); flex: none; }
  .partner-youth { left: 20px; top: 127px; width: 171px; height: 118px; font-size: 19px; line-height: 1.2; }
  .partner-info { left: 20px; top: 266px; width: 315px; height: 79px; font-size: 22px; }
  .partner-region { left: 837px; top: 264px; width: 300px; height: 85px; font-size: 24px; }
</style>
</head>
<body>
<div class="canvas">
  <section class="banner">
    <h1 class="award-title">FRESH HORIZONS AWARD</h1>

    <div class="year-tag">
      <svg width="175" height="62" viewBox="0 0 175 62"><polygon points="0,6 175,0 168,62 8,56" fill="#16b49c"/></svg>
      <span>2019</span>
    </div>

    <p class="tagline">ein regionaler Preis für innovative Jugendprojekte</p>

    <p class="eligibility">
      <span class="caps">Einreichen können Jugendliche zwischen 12 und 26 Jahren,</span><br>
      VertreterInnen von Gemeinden, Institutionen, Verbänden und Vereinen
    </p>

    <p class="highlight">Die 3 innovativsten Einreichungen werden prämiert</p>

    <div class="event-date">
      <svg width="418" height="79" viewBox="0 0 418 79"><polygon points="6,0 418,6 404,79 0,72" fill="#16b49c"/></svg>
      <p><span>Donnerstag, 19. September</span><span>von 17:00 – 20:00 Uhr</span></p>
    </div>

    <div class="partner partner-youth"><span>Jugendbüro Talregion</span></div>
    <div class="partner partner-info"><span class="mark"></span><span>Talregion Infopunkt</span></div>
    <div class="partner partner-region"><span>Hügelland Süd</span></div>
  </section>
</div>
</body>
</html>
```